New Business Card Design Project

I would like my card design to look exactly like the logo, design, layout, and print of the current attached file. The only change I would like made would be for the print to say THE KMW GROUP instead of THE HALLORAN GROUP. Basically, just replace his group name with my group name. I would also like the backgroud to be the same texture and color as the attached file. I love the dark blue lettering and house logo on the card.

I am completely open to the rest of the card design. I just want something clean and simple. Only basic contact info required on the card. Maybe just name: Kyle M Warrick and cell # 555.914.2087 and email kyle@orchidhomesagent.com

```html
<!DOCTYPE html>
<html lang="en">
<head>
<meta charset="utf-8">
<title>The KMW Group – Business Card</title>
<link rel="stylesheet" href="https://fonts.googleapis.com/css2?family=Lato:wght@400;700&display=swap">
<style>
  :root {
    --page-bg: #ffffff;
    --card-bg: #181728;
    --ink-light: #f2f2f2;
  }
  * { margin: 0; padding: 0; box-sizing: border-box; }
  html, body {
    width: 1200px;
    height: 1200px;
    overflow: hidden;
    background: var(--page-bg);
    font-family: "Lato", sans-serif;
    color: var(--ink-light);
  }
  .canvas {
    position: relative;
    width: 1200px;
    height: 1200px;
  }
  .card {
    position: absolute;
    left: 252px;
    width: 631px;
    height: 382px;
    background: var(--card-bg);
    border-radius: 22px;
  }
  .card--front { top: 202px; }
  .card--back  { top: 610px; }

  .brand {
    position: absolute;
    left: 388px;
    top: 260px;
    display: flex;
    align-items: center;
    gap: 30px;
  }
  .brand__square {
    width: 80px;
    height: 80px;
    background: var(--ink-light);
  }
  .brand__name {
    font-size: 21px;
    font-weight: 400;
    line-height: 26px;
    letter-spacing: 4px;
    color: var(--ink-light);
  }
  .brand__name span { display: block; }

  .contact {
    position: absolute;
    left: 44px;
    top: 126px;
  }
  .contact__name {
    font-size: 24px;
    font-weight: 700;
    letter-spacing: 1.2px;
    text-transform: uppercase;
    margin-bottom: 42px;
  }
  .contact__row {
    display: flex;
    align-items: center;
    gap: 10px;
    font-size: 19px;
    font-weight: 400;
    line-height: 32px;
  }
  .contact__icon {
    width: 18px;
    height: 18px;
    flex: none;
  }
</style>
</head>
<body>
<main class="canvas">
  <section class="card card--front" aria-label="Card front">
    <div class="brand">
      <div class="brand__square" aria-hidden="true"></div>
      <p class="brand__name"><span>THE</span><span>KMW</span><span>GROUP</span></p>
    </div>
  </section>

  <section class="card card--back" aria-label="Card back">
    <div class="contact">
      <h1 class="contact__name">Kyle M Warrick</h1>
      <p class="contact__row">
        <svg class="contact__icon" viewBox="0 0 18 18" aria-hidden="true">
          <path d="M2 7c0-2 3-3.5 7-3.5S16 5 16 7v1.5h-3.5V7h-7v1.5H2z" fill="#f2f2f2"/>
          <path d="M5 9h8l1.5 5.5h-11z" fill="#f2f2f2"/>
          <circle cx="9" cy="12" r="1.6" fill="#181728"/>
        </svg>
        <span>555.914.2087</span>
      </p>
      <p class="contact__row">
        <svg class="contact__icon" viewBox="0 0 18 18" aria-hidden="true">
          <rect x="1.5" y="6" width="15" height="10" fill="none" stroke="#f2f2f2" stroke-width="1.2"/>
          <path d="M1.5 6l7.5 6 7.5-6M4 7.5V2.5h10v5" fill="none" stroke="#f2f2f2" stroke-width="1.2"/>
        </svg>
        <span>kyle@orchidhomesagent.com</span>
      </p>
    </div>
  </section>
</main>
</body>
</html>
```